New design of old website

We need a new design of our domain name reseller website.

quilanorte.com

we would also like new design for Logo and all.

the site will be in English and portuguesse,

Industry/Entity Type

Domain

```html
<!DOCTYPE html>
<html lang="en">
<head>
<meta charset="utf-8">
<title>quilanorte — Domain Reseller</title>
<link rel="stylesheet" href="https://fonts.googleapis.com/css2?family=Fira+Sans+Condensed:ital,wght@0,400;0,500;0,600;1,500;1,600&family=Source+Sans+3:ital,wght@0,400;0,600;1,400&display=swap">
<style>
:root{
  --blue:#0d5a9c;
  --blue-dark:#07355f;
  --nav-top:#0e5aa0;
  --nav-bottom:#063a6d;
  --band:#444546;
  --green:#5d9c2a;
  --text-grey:#555;
  --footer-grey:#4a4b4c;
  --white:#fff;
}
*{margin:0;padding:0;box-sizing:border-box}
html,body{width:1200px;height:1169px;overflow:hidden}
body{position:relative;background:linear-gradient(#fff 445px,#f3f3f3 700px,#e6e6e6 1010px);font-family:"Source Sans 3",sans-serif;color:var(--text-grey)}
.abs{position:absolute}
.header{left:0;top:0;width:1200px;height:88px;background:linear-gradient(#fff,#f2f2f2);border-top:2px solid var(--nav-top)}
.brand{left:162px;top:22px;display:flex;align-items:center;gap:10px}
.brand-mark{width:34px;height:34px;background:var(--blue)}
.brand-name{font-family:"Source Sans 3",sans-serif;font-weight:600;font-size:40px;color:var(--blue);line-height:1}
.lang{top:31px;font-size:12px;color:var(--blue)}
.search{left:872px;top:20px;width:159px;height:35px;background:linear-gradient(#fff,#eee);border:1px solid #d6d6d6;box-shadow:0 2px 3px rgba(0,0,0,.15);font-size:12px;color:var(--blue);padding:9px 12px}
.search svg{position:absolute;right:10px;top:8px}
.nav{left:0;top:88px;width:1200px;height:26px;background:linear-gradient(var(--nav-top),var(--nav-bottom))}
.nav-list{position:absolute;left:174px;top:0;display:flex;list-style:none;height:26px}
.nav-list li{font-family:"Fira Sans Condensed",sans-serif;font-weight:400;font-size:13px;color:var(--white);line-height:26px;padding:0 14px;border-right:1px solid rgba(255,255,255,.35);white-space:nowrap}
.nav-list li:last-child{border-right:none}
.nav-follow{right:165px;top:0;height:26px;display:flex;align-items:center;gap:10px}
.follow{font-family:"Fira Sans Condensed",sans-serif;font-size:13px;color:var(--white);white-space:nowrap}
.social{display:flex;gap:9px}
.social span{width:18px;height:18px;border-radius:3px;display:block}
.s1{background:#3b5b9a}.s2{background:#30a9de}.s3{background:#1d7ab5}.s4{background:#f08a1e}
.band{left:0;top:114px;width:1200px;height:331px;background:var(--band)}
.slider{left:157px;top:129px;width:876px;height:314px;background:linear-gradient(135deg,#fff,#e8e8e8);border-bottom:3px solid #333}
.slide-title{left:274px;top:184px;font-family:"Fira Sans Condensed",sans-serif;font-style:italic;font-weight:600;font-size:42px;color:var(--blue)}
.slide-sub{left:274px;top:242px;font-family:"Fira Sans Condensed",sans-serif;font-style:italic;font-weight:600;font-size:26px;line-height:32px;color:#555}
.slide-btn{left:276px;top:318px;height:35px;padding:0 9px;background:linear-gradient(#6fb334,#4f8a22);color:#fff;font-family:"Fira Sans Condensed",sans-serif;font-weight:600;font-size:16px;line-height:35px;text-align:center;border-radius:2px;white-space:nowrap;letter-spacing:-.2px}
.arrow{top:256px;width:60px;height:60px;border-radius:50%;background:#3a3a3a}
.arrow span{position:absolute;left:17px;top:17px;width:26px;height:26px;border-radius:50%;background:#fff}
.key-art{left:665px;top:146px;width:295px;height:362px;background:radial-gradient(ellipse at 55% 60%,#fafafa,#cfcfcf 70%,rgba(220,220,220,0) 72%)}
.features{left:160px;top:523px;width:877px;height:212px;background:#e9e9e9;box-shadow:0 6px 8px -6px rgba(0,0,0,.3)}
.feature{top:534px;width:196px}
.feature-photo{width:196px;height:116px;border:1px solid #ccc}
.feature h3{font-weight:400;font-size:19px;color:var(--blue);margin:11px 0 3px 2px}
.feature p{font-style:italic;font-size:14px;line-height:18px;color:#666;margin-left:3px}
.footer{left:0;top:1010px;width:1200px;height:159px;background:radial-gradient(ellipse 350px 120px at 600px 40px,#8d8e90,var(--footer-grey) 100%)}
.why{left:160px;top:761px;width:877px;height:280px;background:linear-gradient(#0b5596,var(--blue-dark));box-shadow:0 4px 8px rgba(0,0,0,.35)}
.why-photo{left:182px;top:785px;width:244px;height:161px;background:radial-gradient(circle at 50% 55%,#7fc0da 0,#4a97bb 22%,#e6e6e6 35%,#fff 75%)}
.why-title{left:460px;top:780px;font-family:"Fira Sans Condensed",sans-serif;font-weight:600;font-size:25px;color:#fff}
.why-sub{left:460px;top:814px;font-family:"Fira Sans Condensed",sans-serif;font-style:italic;font-weight:500;font-size:19px;color:#fff}
.why-text{left:461px;top:849px;width:548px;font-size:11.5px;line-height:16.6px;color:#fff}
.why-text p{margin-bottom:9px}
.badge{background:#5f6062}
.foot-follow{right:164px;top:1061px;font-size:14px;color:#fff}
.foot-social{left:932px;top:1089px}
.foot-social span{width:20px;height:20px}
.foot-line{left:0;top:1127px;width:1200px;height:1px;background:#5c5d5e}
.foot-nav{left:160px;top:1141px;font-size:11px;color:#ddd;word-spacing:2px}
.copyright{right:164px;top:1141px;font-size:11px;color:#ddd}
</style>
</head>
<body>
<header class="abs header">
  <div class="abs brand"><span class="brand-mark"></span><span class="brand-name">quilanorte</span></div>
  <span class="abs lang" style="left:750px">English</span>
  <span class="abs lang" style="left:801px">Portuguese</span>
  <div class="abs search">Search
    <svg width="18" height="18" viewBox="0 0 18 18"><circle cx="7" cy="7" r="5" fill="none" stroke="#777" stroke-width="2"/><line x1="11" y1="11" x2="16" y2="16" stroke="#777" stroke-width="3"/></svg>
  </div>
</header>
<nav class="abs nav">
  <ul class="nav-list">
    <li>HOME</li><li>WHY QUILANORTE</li><li>PRODUCTS</li><li>SERVICES</li><li>RESELLER</li><li>CONTACT</li><li>LOGIN</li>
  </ul>
  <div class="abs nav-follow">
    <span class="follow">Follow Us On</span>
    <div class="social"><span class="s1"></span><span class="s2"></span><span class="s3"></span><span class="s4"></span></div>
  </div>
</nav>
<div class="abs band"></div>
<section class="abs slider"></section>
<div class="abs arrow" style="left:139px"><span></span></div>
<div class="abs arrow" style="left:994px"><span></span></div>
<h1 class="abs slide-title">Security</h1>
<p class="abs slide-sub">More than 15 years of experience<br>in the domain name business.</p>
<div class="abs slide-btn">Get to know our services.</div>
<div class="abs key-art" role="img" aria-label="Silver key standing in a keyboard Enter key"></div>

<section class="abs features"></section>
<div class="abs feature" style="left:176px">
  <div class="feature-photo" role="img" aria-label="Businessman touching a glowing security interface" style="background:linear-gradient(90deg,#5b4d43,#8fa6b0 60%,#4fb8d4)"></div>
  <h3>Security</h3><p>Protecting your brand against undesire assicaiation.</p>
</div>
<div class="abs feature" style="left:390px">
  <div class="feature-photo" role="img" aria-label="Business partners shaking hands" style="background:linear-gradient(90deg,#8a8a86,#cfc9bd 50%,#9fb4c8)"></div>
  <h3>TLD Expecilist</h3><p>Providing a large portfolio for your clients.</p>
</div>
<div class="abs feature" style="left:606px">
  <div class="feature-photo" role="img" aria-label="Man in front of a network diagram" style="background:linear-gradient(#6f756c,#3f4540)"></div>
  <h3>Automation</h3><p>Domain Process : Quicl and Reli-able.</p>
</div>
<div class="abs feature" style="left:818px">
  <div class="feature-photo" role="img" aria-label="Support agent with a headset" style="background:linear-gradient(90deg,#3f8fc4,#cfe0ec 50%,#e8e8e8)"></div>
  <h3>Personal Service</h3><p>High qualified professional at your service.</p>
</div>

<footer class="abs footer"></footer>
<section class="abs why"></section>
<div class="abs why-photo" role="img" aria-label="Glass globe held in an open hand"></div>
<h2 class="abs why-title">WHY QUILANORTE</h2>
<p class="abs why-sub">GIVE YOUR CUSTOMERS A CHOICE OF 250 TOP LEVEL DOMAINS (TLDS)</p>
<div class="abs why-text">
  <p>Quilanorte is mainly focused the the latin american marked. Today Quilanorte is the fastest growing .br registrar and today many of the world’s largest registrars are using Quilanic to register .br domain with or without local present. With the unique QuilaNIC registration engine, you can offer your customers more than 200 top-level domains (TLDs).</p>
  <p>t is ideal for companies wishing to go beyond the usual narrow range of TLDs and differentiate themselves from competitors by offering a much larger portfolio. Your customers can register domains worldwide through one user-friendly interface. It is easily integrated into your existing order provisioning system, using our XML API, Quilanorte Web Service, or standard email templates. You can also submit orders directly through the Quilanorte web interface. Our local presence services mean you can offer your customers everything they are likely to want – including restricted TLDs in countries where a presence on the ground is required.</p>
</div>

<div class="abs badge" style="left:160px;top:1062px;width:68px;height:41px"></div>
<div class="abs badge" style="left:255px;top:1073px;width:159px;height:26px"></div>
<span class="abs foot-follow">Follow Us On</span>
<div class="abs social foot-social"><span class="s1"></span><span class="s4"></span><span class="s2"></span><span class="s3"></span></div>
<div class="abs foot-line"></div>
<div class="abs foot-nav">HOME \ WHY QUILANORTE \ PRODUCTS \ SERVICES \ RESELLER \ CONTACT \ LOGIN</div>
<div class="abs copyright">Copyrights @ 2013 All Rights Reserved</div>
</body>
</html>
```